Business Card Design

We would like a business card that utilizes our current logo and keeps with the same feel - elegant and organic. Our farm isn't about mass production, it's about excellence, education, beautiful events and flowers - people, culture, and community.

Target Market(s)

Patrons to our farm who are interested in weddings, events, or our flowers and vegetables.

Contact Information for Business Card

Name, address, cell email (Rosalind Hepworth, 2718 Wintervale Rd, Longmont, CO 80517, cell 30.412.6387, email rosalind@wintervalefarm.example)

```html
<!DOCTYPE html>
<html lang="en">
<head>
<meta charset="utf-8">
<title>Wintervale Farm – Business Card</title>
<link rel="stylesheet" href="https://fonts.googleapis.com/css2?family=Lato:wght@300;400&family=Roboto:wght@400;500&display=swap">
<style>
  :root {
    --backdrop: #ecebe7;
    --card-white: #ffffff;
    --sage: #6f8770;
    --sage-deep: #5e7661;
    --sage-card: #728873;
    --sage-mark: #9db09d;
    --ink: #2f2f2f;
    --label: #7b8e7b;
  }
  html, body {
    margin: 0;
    padding: 0;
    width: 900px;
    height: 1200px;
    overflow: hidden;
    background: var(--backdrop);
  }
  .canvas {
    position: relative;
    width: 900px;
    height: 1200px;
  }
  .card {
    position: absolute;
    left: 80px;
    width: 742px;
    height: 440px;
    border-radius: 40px;
    box-shadow: 0 6px 14px rgba(0, 0, 0, 0.25);
    overflow: hidden;
  }
  .card--front { top: 132px; background: var(--card-white); }
  .card--back  { top: 638px; background: var(--sage-card); }

  .brand-name {
    position: absolute;
    left: 0;
    right: 0;
    text-align: center;
    font-family: "Lato", sans-serif;
    font-weight: 300;
    letter-spacing: 4px;
    white-space: nowrap;
  }
  .card--front .brand-name { top: 112px; font-size: 58px; color: var(--sage); }
  .card--back .brand-name  { top: 118px; font-size: 58px; color: var(--sage-mark); }

  .holder {
    position: absolute;
    right: 400px;
    top: 288px;
    text-align: right;
  }
  .holder__name {
    font-family: "Roboto", sans-serif;
    font-weight: 500;
    font-size: 26px;
    color: var(--sage);
    line-height: 1;
  }
  .holder__role {
    margin-top: 8px;
    font-family: "Lato", sans-serif;
    font-size: 15px;
    color: var(--ink);
  }
  .divider {
    position: absolute;
    left: 364px;
    top: 288px;
    width: 1.5px;
    height: 58px;
    background: var(--sage);
  }
  .contact {
    position: absolute;
    left: 382px;
    top: 286px;
    margin: 0;
    padding: 0;
    list-style: none;
    font-family: "Lato", sans-serif;
    font-size: 15.5px;
    color: var(--ink);
  }
  .contact li {
    display: flex;
    align-items: center;
    height: 20px;
  }
  .contact svg {
    width: 13px;
    height: 13px;
    margin-right: 12px;
    fill: var(--sage-deep);
  }
  .services {
    position: absolute;
    left: 0;
    right: 0;
    top: 382px;
    margin: 0;
    padding: 0;
    list-style: none;
    display: flex;
    justify-content: center;
    gap: 26px;
    font-family: "Lato", sans-serif;
    font-size: 16px;
    letter-spacing: 1px;
    color: var(--label);
  }
  .services li::before {
    content: "";
    display: inline-block;
    width: 5px;
    height: 5px;
    margin-right: 9px;
    border-radius: 50%;
    background: var(--sage);
    vertical-align: middle;
  }
</style>
</head>
<body>
<main class="canvas">
  <section class="card card--front">
    <div class="brand-name">Wintervale Farm</div>

    <div class="holder">
      <div class="holder__name">Rosalind Hepworth</div>
      <div class="holder__role">Owner</div>
    </div>
    <div class="divider"></div>

    <ul class="contact">
      <li>
        <svg viewBox="0 0 16 16" aria-hidden="true"><path d="M1 5c0-2 3-3 7-3s7 1 7 3v1h-4V4.5H5V6H1zM3 7h10l1 7H2z"/></svg>
        303.412.6387 All
      </li>
      <li>
        <svg viewBox="0 0 16 16" aria-hidden="true"><path d="M1 3h14v10H1zM2 4l6 5 6-5v1l-6 5-6-5z"/></svg>
        rosalind@wintervalefarm.example
      </li>
      <li>
        <svg viewBox="0 0 16 16" aria-hidden="true"><circle cx="8" cy="8" r="7"/></svg>
        @wintervalefarm
      </li>
    </ul>

    <ul class="services">
      <li>WEDDINGS</li>
      <li>EVENTS</li>
      <li>FLOWERS</li>
      <li>MARKETS</li>
    </ul>
  </section>

  <section class="card card--back">
    <div class="brand-name">Wintervale Farm</div>
  </section>
</main>
</body>
</html>
```